Taomeng business card -we import and distributed Chinese herbal medicine into Australia for prac...

We need a business card for our recently purchased and rebranded company. We are a small family run business - husband and wife team. Our logo is red and black, and we would like the card to be white, with an element of gold in the design (the first cloud in the attached png) which when printed we would like embossed in gold. Our website uses Chinese water colour paintings in the banners (www.taomeng.net.au) so a design that is in harmony with this would be ideal.
side one needs to include:

Target Market(s)

potential customers

Industry/Entity Type

Health And Wellness

Contact Information for Business Card

Side 1
logo,
Edmund Varsk Director
Practitioner Support and Education
0491 722 413
edmund@taomeng.net.au
218 Colbury St, Harrowdale, WA, 6185

side 2 needs to include:
logo
Priscilla Moult Director
Orders, Accounts and Despatch
0487 530 619
priscilla@taomeng.net.au

Font styles to use
Serif

Colors

Designer to choose colors to be used in the design.

Requirements
Must have
• black, red, gold colours
Nice to have
• we like the font papyrus (mac font)

```html
<!DOCTYPE html>
<html lang="en">
<head>
<meta charset="utf-8">
<title>Taomeng Business Cards</title>
<link rel="stylesheet" href="https://fonts.googleapis.com/css2?family=Tinos:wght@400;700&display=swap">
<style>
  :root {
    --backdrop: #7a5f45;
    --card-light: #ffffff;
    --seal-red: #d93a22;
    --accent-red: #e0402a;
    --gold: #f2c14e;
    --gold-rule: #b59a5a;
    --navy: #1f2340;
    --white: #ffffff;
  }
  * { margin: 0; padding: 0; box-sizing: border-box; }
  html, body { width: 900px; height: 1200px; overflow: hidden; }
  body {
    background: var(--backdrop);
    font-family: "Tinos", "Times New Roman", serif;
    position: relative;
  }
  .card {
    position: absolute;
    left: 80px;
    width: 734px;
    height: 430px;
    border-radius: 24px;
    box-shadow: 0 8px 18px rgba(0,0,0,0.35);
  }
  .card--front { top: 127px; background: linear-gradient(180deg, #050505 0%, #1a1a1a 100%); }
  .card--back { top: 645px; background: var(--card-light); }

  .brand {
    position: absolute;
    display: flex;
    align-items: center;
    gap: 13px;
  }
  .brand__mark {
    width: 56px;
    height: 120px;
    background: var(--seal-red);
  }
  .brand__name {
    font-size: 62px;
    font-weight: 400;
    letter-spacing: 4px;
    line-height: 64px;
  }
  .card--front .brand { left: 236px; top: 86px; }
  .card--front .brand__name { color: var(--gold); }
  .card--back .brand { left: 222px; top: 76px; }
  .card--back .brand__name { color: var(--navy); }

  .rule { position: absolute; height: 2px; }
  .card--front .rule { left: 49px; right: 42px; top: 285px; background: var(--gold-rule); }
  .card--back .rule { left: 44px; right: 46px; top: 283px; background: var(--accent-red); }

  .person { position: absolute; }
  .person__name { font-size: 23px; line-height: 26px; }
  .person__role { font-size: 18px; line-height: 23.5px; color: var(--accent-red); }
  .card--front .person { left: 49px; top: 301px; }
  .card--front .person__name { color: var(--white); }
  .card--back .person { left: 44px; top: 298px; }
  .card--back .person__name { color: var(--navy); font-weight: 700; }
  .card--back .person__role { font-weight: 700; }

  .contacts { position: absolute; list-style: none; font-size: 18px; }
  .contacts li { display: flex; align-items: center; height: 24.5px; gap: 9px; }
  .card--front .contacts { right: 42px; top: 301px; color: var(--white); }
  .card--front .contacts li { justify-content: flex-end; }
  .card--back .contacts { left: 378px; top: 297px; color: var(--navy); }
  .icon { width: 18px; height: 18px; flex: none; }
</style>
</head>
<body>
  <section class="card card--front">
    <div class="brand">
      <div class="brand__mark"></div>
      <div class="brand__name">TAO<br>MENG</div>
    </div>
    <div class="rule"></div>
    <div class="person">
      <div class="person__name">PRISCILLA MOULT</div>
      <div class="person__role">Director</div>
      <div class="person__role">Orders, Accounts and Despatch</div>
    </div>
    <ul class="contacts">
      <li>0487 530 619
        <svg class="icon" viewBox="0 0 18 18"><rect width="18" height="18" rx="2" fill="#d93a22"/><path d="M5 4l2 0 1 3-1.3 1a7 7 0 0 0 3.3 3.3l1-1.3 3 1v2c0 .6-.5 1-1 1A9 9 0 0 1 4 5c0-.5.4-1 1-1z" fill="#fff"/></svg></li>
      <li>priscilla@taomeng.net.au
        <svg class="icon" viewBox="0 0 18 18"><rect width="18" height="18" rx="2" fill="#d93a22"/><rect x="4" y="5.5" width="10" height="7" fill="none" stroke="#fff" stroke-width="1.3"/><path d="M4 5.5l5 4 5-4" fill="none" stroke="#fff" stroke-width="1.3"/></svg></li>
      <li>218 Colbury St, Harrowdale, WA, 6185
        <svg class="icon" viewBox="0 0 18 18"><rect width="18" height="18" rx="2" fill="#d93a22"/><path d="M9 3.5a4 4 0 0 1 4 4c0 3-4 7-4 7s-4-4-4-7a4 4 0 0 1 4-4z" fill="#fff"/><circle cx="9" cy="7.5" r="1.5" fill="#d93a22"/></svg></li>
    </ul>
  </section>

  <section class="card card--back">
    <div class="brand">
      <div class="brand__mark"></div>
      <div class="brand__name">TAO<br>MENG</div>
    </div>
    <div class="rule"></div>
    <div class="person">
      <div class="person__name">EDMUND VARSK</div>
      <div class="person__role">Director</div>
      <div class="person__role">Practitioner Support and Education</div>
    </div>
    <ul class="contacts">
      <li><svg class="icon" viewBox="0 0 18 18"><rect width="18" height="18" rx="2" fill="#d93a22"/><path d="M5 4l2 0 1 3-1.3 1a7 7 0 0 0 3.3 3.3l1-1.3 3 1v2c0 .6-.5 1-1 1A9 9 0 0 1 4 5c0-.5.4-1 1-1z" fill="#fff"/></svg>0491 722 413</li>
      <li><svg class="icon" viewBox="0 0 18 18"><rect width="18" height="18" rx="2" fill="#d93a22"/><rect x="4" y="5.5" width="10" height="7" fill="none" stroke="#fff" stroke-width="1.3"/><path d="M4 5.5l5 4 5-4" fill="none" stroke="#fff" stroke-width="1.3"/></svg>edmund@taomeng.net.au</li>
      <li><svg class="icon" viewBox="0 0 18 18"><rect width="18" height="18" rx="2" fill="#d93a22"/><path d="M9 3.5a4 4 0 0 1 4 4c0 3-4 7-4 7s-4-4-4-7a4 4 0 0 1 4-4z" fill="#fff"/><circle cx="9" cy="7.5" r="1.5" fill="#d93a22"/></svg>218 Colbury St, Harrowdale, WA, 6185</li>
    </ul>
  </section>
</body>
</html>
```